Business card design needed

New company based in Brisbane, Australia. Brindle Systems. The business is focused on the delivery of network architecture design and deployment. We will provide both services and the sale of the necessary equipment to deliver the service. Cloud computing is an important element of our focus as this is an emerging market for enterprises in Queensland. Our target marketplace is medium to large corporations with complex infrastructure requirements. IT Management and above will be the typical entry point for us into these accounts. We would like to see the use of various shade of green, design should be clutter free and impress stability, trust and growth.
Updates
Hey Everyone
Just we let you all know we have changed this project to 'committed' payment status.
Looking forward to seeing the designs! Thanks for your efforts.
Best Regards
Marcus
Industry/Entity Type
Architecture
Contact Information for Business Card
Brindle Systems, Marcus Doyle, Sales Director, Level 14 Harlow Tower, 58 Penfold Street, Brisbane QLD 4000, Ph +61 7 3904 2267, M +61 4 4926 1573, E marcus.doyle@brindlesystems-example.com.au
Look and feel
Each slider illustrates characteristics of the customer's brand and the style your logo design should communicate.

```html
<!DOCTYPE html>
<html lang="en">
<head>
<meta charset="utf-8">
<title>Brindle Systems – Marcus Doyle</title>
<link rel="stylesheet" href="https://fonts.googleapis.com/css2?family=Heebo:wght@300&display=swap">
<style>
  :root {
    --ink: #3a9447;
    --rule: #7dc27f;
    --mark: #a9d99c;
    --paper: #ffffff;
  }
  * { margin: 0; padding: 0; box-sizing: border-box; }
  html, body { width: 1200px; height: 691px; overflow: hidden; background: var(--paper); }
  .card {
    position: relative;
    width: 1200px;
    height: 691px;
    background: var(--paper);
    font-family: "Heebo", "Helvetica Neue", Arial, sans-serif;
    font-weight: 300;
    color: var(--ink);
  }
  .brand {
    position: absolute;
    left: 100px;
    top: 88px;
    width: 250px;
    text-align: center;
  }
  .brand-dot {
    display: block;
    width: 150px;
    height: 150px;
    margin: 0 auto 28px;
    border-radius: 50%;
    background: var(--mark);
  }
  .brand-name { font-size: 30px; line-height: 1; white-space: nowrap; }
  .person {
    position: absolute;
    left: 738px;
    top: 196px;
    width: 462px;
    padding-left: 24px;
    padding-bottom: 16px;
    border-bottom: 1.5px solid var(--rule);
  }
  .person-name { font-size: 39px; line-height: 48px; font-weight: 300; }
  .person-title { font-size: 29px; line-height: 38px; font-style: italic; }
  .details {
    position: absolute;
    left: 70px;
    top: 378px;
    width: 718px;
  }
  .address {
    font-style: normal;
    font-size: 30px;
    line-height: 40px;
    padding-left: 9px;
    padding-bottom: 6px;
    border-bottom: 1.5px solid var(--rule);
  }
  .contact { list-style: none; padding-left: 9px; padding-top: 6px; font-size: 30px; line-height: 40px; }
  .contact-label { display: inline-block; width: 46px; }
</style>
</head>
<body>
  <main class="card">
    <div class="brand">
      <span class="brand-dot"></span>
      <span class="brand-name">Brindle Systems</span>
    </div>

    <header class="person">
      <h1 class="person-name">Marcus Doyle</h1>
      <p class="person-title">Sales Director</p>
    </header>

    <section class="details">
      <address class="address">
        Level 14 Harlow Tower,<br>
        58 Penfold Street,<br>
        Brisbane QLD 4000
      </address>
      <ul class="contact">
        <li><span class="contact-label">P.</span>+61 7 3904 2267</li>
        <li><span class="contact-label">M.</span>+61 4 4926 1573</li>
        <li><span class="contact-label">E.</span>marcus.doyle@brindlesystems-example.com.au</li>
      </ul>
    </section>
  </main>
</body>
</html>
```